Brisco Skiff Ferry and Haulage Business Card

I need business cards for my new water taxi and freight transport business I have started here in Kodiak Alaska. Kodiak is a remote island in the middle of the gulf of Alaska. There are seven native villages around the island and Kodiak is the #2 fishing port in the United States. We also have the largest Harbor Watch Base in the U.S. My company will be providing water taxi and freight transport logistics to the villages and many hunting and fishing lodges as well as remote properties around the island.

I would like a business card that isn't status quo, something that stands out, either in feel or appearance. I do like clean minimal designs but it needs to have the necessary contact info on it.

Target Market(s)

remote lodge / property owners, residents of the many villages around Kodiak and any one wanting to enjoy the great outdoors of Kodiak Alaska

Industry/Entity Type

Business

Contact Information for Business Card

I like clean simple designs that aren't cluttered but still provide the necessary information

Colors
0255a3
3277b5
33a4d5
9bcb3c
add136
fbed22
ffc214
f78f20
f37122

Requirements
Must have
• logo and contact info
• Captain Wade Pemberton
• www.briscoskiffferry.net
• wade@briscoskiffferry.net

```html
<!DOCTYPE html>
<html lang="en">
<head>
<meta charset="utf-8">
<title>Brisco Skiff Ferry and Haulage – Business Card</title>
<link rel="stylesheet" href="https://fonts.googleapis.com/css2?family=Michroma&family=Open+Sans:wght@400;600&display=swap">
<style>
  :root {
    --page-bg: #e9e6e1;
    --card-bg: #ffffff;
    --navy: #2d4a9b;
    --sky: #4fa6da;
    --orange: #f7a028;
    --orange-light: #fcc46a;
    --ink: #2b2a26;
  }
  * { box-sizing: border-box; margin: 0; padding: 0; }
  html, body {
    width: 1200px; height: 1200px; overflow: hidden;
    background: var(--page-bg);
  }
  .sheet {
    width: 1200px; height: 1200px;
    display: flex; flex-direction: column;
    align-items: center; justify-content: center; gap: 60px;
  }
  .card {
    position: relative;
    width: 880px; height: 503px;
    background: var(--card-bg);
    box-shadow: 0 6px 18px rgba(0,0,0,.18);
    overflow: hidden;
  }

  /* Front */
  .front-brand {
    position: absolute; left: 0; right: 0; top: 110px;
    display: flex; align-items: center; justify-content: center; gap: 26px;
  }
  .brand-dot {
    width: 70px; height: 70px; border-radius: 50%;
    background: var(--orange);
    flex: none;
  }
  .brand-name {
    font-family: "Michroma", sans-serif;
    font-size: 38px; line-height: 1.3;
    color: var(--navy);
    max-width: 560px;
  }
  .front-band {
    position: absolute; left: 0; right: 0; bottom: 60px; height: 78px;
    background: linear-gradient(180deg, var(--orange) 0%, var(--orange-light) 100%);
    display: flex; align-items: center; justify-content: center;
  }
  .front-web {
    font-family: "Open Sans", sans-serif; font-weight: 600;
    font-size: 34px; letter-spacing: 1px;
    color: var(--ink);
  }

  /* Back */
  .holder-name {
    position: absolute; left: 60px; top: 150px;
    font-family: "Michroma", sans-serif;
    font-size: 50px; letter-spacing: 2px;
    color: var(--navy);
  }
  .holder-role {
    position: absolute; right: 120px; top: 232px;
    font-family: "Open Sans", sans-serif; font-weight: 400;
    font-size: 44px; letter-spacing: 2px;
    color: var(--sky);
  }
  .contact-line {
    position: absolute; left: 60px; bottom: 70px;
    font-family: "Open Sans", sans-serif; font-weight: 400;
    font-size: 28px; color: var(--orange);
    display: flex; gap: 16px; align-items: center;
  }
  .contact-sep { color: var(--sky); font-weight: 600; }
</style>
</head>
<body>
<main class="sheet">
  <section class="card card-front">
    <div class="front-brand">
      <span class="brand-dot"></span>
      <span class="brand-name">Brisco Skiff Ferry and Haulage</span>
    </div>
    <div class="front-band">
      <span class="front-web">www.briscoskiffferry.net</span>
    </div>
  </section>

  <section class="card card-back">
    <h1 class="holder-name">WADE PEMBERTON</h1>
    <p class="holder-role">Captain</p>
    <p class="contact-line">
      <span class="contact-email">wade@briscoskiffferry.net</span>
      <span class="contact-sep">|</span>
      <span class="contact-web">www.briscoskiffferry.net</span>
    </p>
  </section>
</main>
</body>
</html>
```